Still River Way - Business Card

May try various combos of colors from primary & secondary palette attached below. Logo and Catch phrase previous built logo attached should go on front, but change to color palette options noted. may try various color options from minimal to zen like quality/vibe.
On Front: Attached Logo & Phrase
On Back:
https://stillriverway.com/
415.555.0193
stillriverway@theremotehelpers.ai

Contact Information for Business Card

Gregory T. Lund, MD Founder & CEO https://stillriverway.com/ 415.555.0193 stillriverway@theremotehelpers.ai

```html
<!DOCTYPE html>
<html lang="en">
<head>
<meta charset="utf-8">
<title>Still River Way – Business Card</title>
<link href="https://fonts.googleapis.com/css2?family=Montserrat:wght@400;700&family=Tinos&display=swap" rel="stylesheet">
<style>
  :root {
    --backdrop: #e9e6e0;
    --card-white: #ffffff;
    --card-grey: #a0a0a0;
    --moss: #485a22;
    --moss-dark: #3d4d1c;
    --ink: #222222;
    --muted: #8a8a8a;
    --silver: #d9d9d9;
    --faint: #f1f1f1;
  }
  * { margin: 0; padding: 0; box-sizing: border-box; }
  html, body { width: 900px; height: 1200px; overflow: hidden; }
  body { background: var(--backdrop); position: relative; font-family: "Montserrat", sans-serif; }

  .card {
    position: absolute;
    left: 80px;
    width: 742px;
    height: 440px;
    border-radius: 38px;
    overflow: hidden;
    box-shadow: 0 6px 14px rgba(0,0,0,0.25);
  }
  .card--front { top: 132px; background: var(--card-white); }
  .card--back  { top: 638px; background: var(--card-grey); }

  /* front */
  .front-ring {
    position: absolute; left: -90px; top: 20px;
    width: 360px; height: 360px; border-radius: 50%;
    border: 3px solid var(--faint);
  }
  .brand-mark {
    position: absolute; left: 491px; top: 40px;
    width: 94px; height: 94px; border-radius: 50%;
    border: 2px solid var(--moss);
  }
  .brand-name {
    position: absolute; left: 300px; width: 474px; top: 160px;
    text-align: center;
    font-family: "Tinos", serif; font-size: 40px; color: var(--moss); line-height: 1;
  }
  .brand-tagline {
    position: absolute; left: 300px; width: 474px; top: 203px;
    text-align: center; font-size: 14px; color: var(--muted);
  }
  .person-name {
    position: absolute; left: 32px; top: 274px;
    font-size: 28px; font-weight: 700; color: var(--moss); line-height: 1;
  }
  .person-role {
    position: absolute; left: 34px; top: 305px;
    font-size: 16px; color: var(--ink);
  }
  .divider {
    position: absolute; left: 35px; top: 330px;
    width: 665px; height: 2px; background: var(--moss-dark);
  }
  .contact-list {
    position: absolute; left: 36px; top: 344px; list-style: none;
    font-size: 16px; color: var(--ink);
  }
  .contact-list li { display: flex; align-items: center; height: 22px; }
  .contact-list svg { width: 14px; height: 14px; margin-right: 13px; fill: var(--moss-dark); }
  .front-band {
    position: absolute; left: 0; bottom: 0; width: 100%; height: 14px;
  }

  /* back */
  .back-ring {
    position: absolute; left: -150px; top: 0;
    width: 470px; height: 470px; border-radius: 50%;
    border: 4px solid var(--silver);
  }
  .back-name {
    position: absolute; right: 38px; top: 334px;
    font-family: "Tinos", serif; font-size: 44px; color: var(--card-white); line-height: 1;
  }
  .back-tagline {
    position: absolute; right: 38px; top: 383px;
    font-size: 16px; color: var(--card-white);
  }
</style>
</head>
<body>

<section class="card card--front">
  <div class="front-ring"></div>
  <div class="brand-mark"></div>
  <div class="brand-name">Still River Way</div>
  <div class="brand-tagline">Nurturing Quiet Minds, Hearts &amp; Spirits</div>

  <div class="person-name">Colin Marsh</div>
  <div class="person-role">CEO &amp; Founder</div>
  <div class="divider"></div>

  <ul class="contact-list">
    <li>
      <svg viewBox="0 0 16 16"><path d="M1 5c0-2 3-3 7-3s7 1 7 3v1h-3V5H4v1H1z"/><path d="M3 7h10l1 7H2z"/></svg>
      415.555.0193
    </li>
    <li>
      <svg viewBox="0 0 16 16"><path d="M1 3h14v2L8 9 1 5z"/><path d="M1 6.5l7 4 7-4V13H1z"/></svg>
      stillriverway@theremotehelpers.ai
    </li>
    <li>
      <svg viewBox="0 0 16 16"><circle cx="8" cy="8" r="7"/></svg>
      www.stillriverway.com
    </li>
  </ul>

  <svg class="front-band" viewBox="0 0 742 14" preserveAspectRatio="none">
    <polygon points="0,0 622,0 608,14 0,14" fill="var(--moss)"/>
    <polygon points="622,0 742,0 742,14 608,14" fill="var(--silver)"/>
  </svg>
</section>

<section class="card card--back">
  <div class="back-ring"></div>
  <div class="back-name">Still River Way</div>
  <div class="back-tagline">Nurturing Quiet Minds, Hearts &amp; Spirits</div>
</section>

</body>
</html>
```